Hybrid education and entertainment company needs help with creating dynamic school worksheets

I'm looking for a skilled individual to create a versatile Microsoft Word template for school worksheets for Lessonvaria. Your task will involve:
- Designing a user-friendly and visually appealing template that can be easily customized for various subjects and grade levels.
- Ensuring the template includes sections for titles, instructions, questions, and space for student responses.
- Incorporating consistent formatting and styles to maintain a professional look across all worksheets.
- Adding placeholders for images, graphics, or interactive elements to enhance engagement.
- Testing the template to ensure compatibility and ease of use for educators.
Your work will help streamline the worksheet creation process, making it easier for educators to develop effective and engaging learning materials.

```html
<!DOCTYPE html>
<html lang="en">
<head>
<meta charset="utf-8">
<title>Lessonvaria Worksheets – Science Template</title>
<link rel="stylesheet" href="https://fonts.googleapis.com/css2?family=Bebas+Neue&family=Montserrat:wght@500;800&family=Oswald:wght@500&display=swap">
<style>
  :root {
    --stage: #9b9b9b;
    --paper: #ffffff;
    --crimson: #ab1b5b;
    --blush: #efd2e1;
    --teal: #0e9b8b;
    --ink: #2f2f2f;
    --line: #555555;
    --pattern: #eeeeee;
    --star: #f08a1c;
  }
  * { margin: 0; padding: 0; box-sizing: border-box; }
  html, body { width: 1200px; height: 677px; overflow: hidden; background: var(--stage); }
  .canvas { position: relative; width: 1200px; height: 677px; }

  .cover {
    position: absolute; left: 40px; top: 43px; width: 418px; height: 591px;
    background: var(--paper); overflow: hidden;
    box-shadow: 0 10px 14px rgba(0,0,0,.28);
  }
  .cover svg, .page svg { position: absolute; inset: 0; width: 100%; height: 100%; }

  .page {
    position: absolute; width: 196px; height: 276px;
    box-shadow: 0 10px 12px rgba(0,0,0,.25);
  }
  .page-pattern { position: absolute; inset: 0; background: var(--pattern); }
  .page-card {
    position: absolute; left: 20px; top: 19px; width: 156px; height: 238px;
    background: var(--paper); border: 1px solid var(--line); border-radius: 8px;
  }
  .illustration { position: absolute; }

  .company-name { font-family: "Montserrat", sans-serif; font-weight: 800; fill: var(--paper); }
  .contact { font-family: "Montserrat", sans-serif; font-weight: 500; fill: var(--paper); }
  .display { font-family: "Bebas Neue", sans-serif; }
  .label { font-family: "Oswald", sans-serif; font-weight: 500; fill: var(--ink); }
  .heading { font-family: "Bebas Neue", sans-serif; fill: var(--crimson); font-size: 17px; }
  .badge-text { font-family: "Oswald", sans-serif; font-weight: 500; fill: var(--paper); font-size: 8px; }
  .rule { stroke: var(--line); stroke-width: .6; }
  .frame { fill: none; stroke: var(--crimson); stroke-width: 1; }
</style>
</head>
<body>
<div class="canvas">

  <!-- Cover -->
  <section class="cover">
    <svg viewBox="0 0 418 591">
      <path d="M34,0 H418 V30 C396,105 300,160 175,160 C95,160 40,130 28,85 C20,50 22,20 34,0 Z" fill="var(--crimson)"/>
      <path d="M0,55 C15,120 80,168 190,172 C280,175 350,140 395,92" fill="none" stroke="var(--crimson)" stroke-width="3"/>
      <path d="M130,150 C200,150 250,140 290,128" fill="none" stroke="var(--paper)" stroke-width="1.2"/>
      <text class="company-name" x="209" y="67" font-size="27" text-anchor="middle" textLength="292" lengthAdjust="spacingAndGlyphs">BRIGHTWAY SCHOOL</text>
      <text class="company-name" x="209" y="100" font-size="27" text-anchor="middle" textLength="244" lengthAdjust="spacingAndGlyphs">&amp; PLAY STUDIOS</text>

      <text class="display" x="200" y="254" font-size="58" fill="var(--crimson)" text-anchor="middle" textLength="278">LESSONVARIA</text>
      <text class="display" x="200" y="336" font-size="84" fill="var(--teal)" text-anchor="middle" textLength="316">WORKSHEETS</text>

      <g class="pencil">
        <path d="M66,354 H300 L360,379 L300,404 H66 Q61,404 61,399 V359 Q61,354 66,354 Z" fill="var(--paper)" stroke="var(--crimson)" stroke-width="3.5" stroke-linejoin="round"/>
        <line x1="94" y1="354" x2="94" y2="404" stroke="var(--crimson)" stroke-width="3"/>
        <path d="M300,354 Q312,379 300,404" fill="none" stroke="var(--crimson)" stroke-width="3"/>
        <path d="M340,371 L360,379 L340,387 Z" fill="var(--crimson)"/>
        <text class="display" x="199" y="392" font-size="34" fill="var(--ink)" text-anchor="middle">SUBJECT: SCIENCE</text>
      </g>

      <text class="display" x="68" y="447" font-size="24" fill="var(--crimson)">NOTE :</text>
      <line x1="123" y1="445" x2="325" y2="445" stroke="var(--ink)" stroke-width=".8"/>
      <line x1="123" y1="469" x2="300" y2="469" stroke="var(--ink)" stroke-width=".8"/>

      <path d="M0,591 L0,572 C40,515 160,478 280,488 C350,494 400,530 418,562 L418,591 Z" fill="var(--crimson)"/>
      <path d="M160,505 C220,492 270,492 310,502" fill="none" stroke="var(--paper)" stroke-width="1.2"/>
      <text class="contact" x="209" y="549" font-size="13" text-anchor="middle">0198 765 432  |  www.lessonvaria-learn.com</text>

      <path d="M28,152 L62,162 M52,152 L62,162 L54,171" fill="none" stroke="#d9559a" stroke-width="2.2" stroke-linecap="round"/>
      <path d="M105,530 L120,504 M112,506 L120,504 L122,512" fill="none" stroke="#f06a24" stroke-width="2.2" stroke-linecap="round"/>
      <path d="M385,510 L372,498 M372,506 L372,498 L380,498" fill="none" stroke="#f06a24" stroke-width="1.8" stroke-linecap="round"/>
    </svg>
    <div class="illustration" role="img" aria-label="Globe doodle" style="left:304px;top:130px;width:48px;height:48px;border-radius:50%;background:#8fe3ef;"></div>
    <div class="illustration" role="img" aria-label="Alarm clock doodle" style="left:181px;top:160px;width:34px;height:36px;border-radius:50%;background:#d6e6fb;"></div>
    <div class="illustration" role="img" aria-label="Science flask doodle" style="left:375px;top:338px;width:30px;height:40px;border-radius:6px;background:#f3d4e3;"></div>
    <div class="illustration" role="img" aria-label="Light bulb doodle" style="left:361px;top:428px;width:26px;height:38px;border-radius:12px;background:#fde2cf;"></div>
    <div class="illustration" role="img" aria-label="Rolled diploma doodle" style="left:14px;top:350px;width:30px;height:48px;border-radius:6px;background:#e2f3cf;"></div>
    <div class="illustration" role="img" aria-label="Protractor doodle" style="left:34px;top:480px;width:28px;height:28px;border-radius:6px;background:#d4f0ee;"></div>
  </section>

  <!-- Page 01: profile -->
  <article class="page" style="left:501px;top:42px;">
    <div class="page-pattern" role="img" aria-label="Light school doodle pattern"></div>
    <div class="page-card"></div>
    <svg viewBox="0 0 196 276">
      <line class="rule" x1="31" y1="42" x2="68" y2="42"/><line class="rule" x1="128" y1="42" x2="165" y2="42"/>
      <text class="heading" x="98" y="48" text-anchor="middle">HI ITS' ME</text>
      <rect x="30" y="60" width="134" height="21" fill="var(--blush)"/>
      <text class="label" x="40" y="74" font-size="7.5">MY NEME IS :</text>
      <rect x="30" y="93" width="134" height="21" fill="var(--blush)"/>
      <text class="label" x="40" y="107" font-size="7.5">I AM IN GRADE :</text>
      <rect x="30" y="130" width="134" height="112" fill="var(--blush)"/>
      <text class="label" x="40" y="146" font-size="7.5">INSERT YOUR PICTURE HERE :</text>
      <rect x="40" y="157" width="76" height="73" fill="var(--paper)"/>
      <circle cx="98" cy="256" r="8" fill="var(--teal)" stroke="var(--paper)" stroke-width="1.2"/>
      <text class="badge-text" x="98" y="259" text-anchor="middle">01</text>
    </svg>
    <div class="illustration" role="img" aria-label="Cartoon schoolgirl waving" style="left:125px;top:143px;width:60px;height:117px;border-radius:26px 26px 10px 10px;background:linear-gradient(#c65a3e,#d9403c 45%,#f4d35e);"></div>
  </article>

  <!-- Page 03: instructions -->
  <article class="page" style="left:729px;top:42px;">
    <div class="page-pattern" role="img" aria-label="Light school doodle pattern"></div>
    <div class="page-card"></div>
    <svg viewBox="0 0 196 276">
      <line class="rule" x1="31" y1="42" x2="56" y2="42"/><line class="rule" x1="140" y1="42" x2="165" y2="42"/>
      <text class="heading" x="98" y="48" text-anchor="middle">INSTRUCTIONS</text>
      <circle class="frame" cx="56" cy="91" r="27"/>
      <text class="label" x="91" y="69" font-size="7.5">LOREM IPSUM :</text>
      <line class="rule" x1="91" y1="82" x2="164" y2="82"/><line class="rule" x1="91" y1="94" x2="164" y2="94"/><line class="rule" x1="91" y1="106" x2="164" y2="106"/>
      <circle class="frame" cx="137" cy="155" r="27"/>
      <text class="label" x="29" y="140" font-size="7.5">LOREM IPSUM :</text>
      <line class="rule" x1="29" y1="153" x2="102" y2="153"/><line class="rule" x1="29" y1="165" x2="102" y2="165"/><line class="rule" x1="29" y1="177" x2="102" y2="177"/>
      <circle class="frame" cx="56" cy="220" r="27"/>
      <text class="label" x="91" y="203" font-size="7.5">LOREM IPSUM :</text>
      <line class="rule" x1="91" y1="215" x2="164" y2="215"/><line class="rule" x1="91" y1="227" x2="164" y2="227"/><line class="rule" x1="91" y1="239" x2="164" y2="239"/>
      <circle cx="98" cy="256" r="8" fill="var(--teal)" stroke="var(--paper)" stroke-width="1.2"/>
      <text class="badge-text" x="98" y="259" text-anchor="middle">03</text>
    </svg>
  </article>

  <!-- Page 05: questions -->
  <article class="page" style="left:958px;top:42px;">
    <div class="page-pattern" role="img" aria-label="Light school doodle pattern"></div>
    <div class="page-card"></div>
    <svg viewBox="0 0 196 276">
      <line class="rule" x1="31" y1="42" x2="60" y2="42"/><line class="rule" x1="136" y1="42" x2="165" y2="42"/>
      <text class="heading" x="98" y="48" text-anchor="middle">QUESTIONS ?</text>
      <circle cx="37" cy="66" r="6" fill="var(--blush)"/>
      <text class="label" x="37" y="69" font-size="7" text-anchor="middle">05</text>
      <text class="label" x="48" y="69" font-size="7">LOREM IPSUM IS SIMPLY DUMMY TEXT ?</text>
      <rect class="frame" x="31" y="83" width="133" height="54" rx="6"/>
      <circle cx="37" cy="155" r="6" fill="var(--blush)"/>
      <text class="label" x="37" y="158" font-size="7" text-anchor="middle">06</text>
      <text class="label" x="48" y="158" font-size="7">LOREM IPSUM IS SIMPLY DUMMY TEXT ?</text>
      <rect class="frame" x="31" y="169" width="133" height="53" rx="6"/>
      <text class="label" x="43" y="243" font-size="6" font-style="italic">TEACHERS SIGNATURE :</text>
      <line class="rule" x1="103" y1="242" x2="164" y2="242"/>
      <circle cx="98" cy="256" r="8" fill="var(--teal)" stroke="var(--paper)" stroke-width="1.2"/>
      <text class="badge-text" x="98" y="259" text-anchor="middle">05</text>
    </svg>
  </article>

  <!-- Page 02: contents -->
  <article class="page" style="left:501px;top:357px;">
    <div class="page-pattern" role="img" aria-label="Light school doodle pattern"></div>
    <div class="page-card"></div>
    <svg viewBox="0 0 196 276">
      <rect x="21" y="20" width="154" height="31" fill="var(--blush)"/>
      <text class="display" x="30" y="40" font-size="10" fill="var(--crimson)">SL NO</text>
      <text class="display" x="97" y="40" font-size="10" fill="var(--crimson)" text-anchor="middle">TITLES</text>
      <text class="display" x="166" y="40" font-size="10" fill="var(--crimson)" text-anchor="end">PAGE NO</text>
      <g class="label" font-size="8">
        <circle cx="39" cy="70" r="9" fill="var(--blush)"/><text x="39" y="73" text-anchor="middle">01</text><line class="rule" x1="57" y1="73" x2="137" y2="73"/><text x="164" y="73" text-anchor="end">02-05</text>
        <circle cx="39" cy="101" r="9" fill="var(--blush)"/><text x="39" y="104" text-anchor="middle">02</text><line class="rule" x1="57" y1="104" x2="137" y2="104"/><text x="164" y="104" text-anchor="end">06-10</text>
        <circle cx="39" cy="133" r="9" fill="var(--blush)"/><text x="39" y="136" text-anchor="middle">03</text><line class="rule" x1="57" y1="136" x2="137" y2="136"/><text x="164" y="136" text-anchor="end">11-20</text>
        <circle cx="39" cy="166" r="9" fill="var(--blush)"/><text x="39" y="169" text-anchor="middle">04</text><line class="rule" x1="57" y1="169" x2="137" y2="169"/><text x="164" y="169" text-anchor="end">21-24</text>
        <circle cx="39" cy="198" r="9" fill="var(--blush)"/><text x="39" y="201" text-anchor="middle">05</text><line class="rule" x1="57" y1="201" x2="137" y2="201"/><text x="164" y="201" text-anchor="end">25-28</text>
        <circle cx="39" cy="231" r="9" fill="var(--blush)"/><text x="39" y="234" text-anchor="middle">06</text><line class="rule" x1="57" y1="234" x2="137" y2="234"/><text x="164" y="234" text-anchor="end">29-30</text>
      </g>
      <circle cx="98" cy="256" r="8" fill="var(--teal)" stroke="var(--paper)" stroke-width="1.2"/>
      <text class="badge-text" x="98" y="259" text-anchor="middle">02</text>
    </svg>
  </article>

  <!-- Page 04: questions -->
  <article class="page" style="left:729px;top:357px;">
    <div class="page-pattern" role="img" aria-label="Light school doodle pattern"></div>
    <div class="page-card"></div>
    <svg viewBox="0 0 196 276">
      <line class="rule" x1="31" y1="42" x2="60" y2="42"/><line class="rule" x1="136" y1="42" x2="165" y2="42"/>
      <text class="heading" x="98" y="48" text-anchor="middle">QUESTIONS ?</text>
      <circle cx="37" cy="66" r="6" fill="var(--blush)"/><text class="label" x="37" y="69" font-size="7" text-anchor="middle">01</text>
      <text class="label" x="48" y="69" font-size="7">LOREM IPSUM IS SIMPLY DUMMY TEXT ?</text>
      <line class="rule" x1="31" y1="87" x2="123" y2="87"/><line class="rule" x1="31" y1="99" x2="123" y2="99"/><line class="rule" x1="31" y1="111" x2="123" y2="111"/>
      <rect class="frame" x="130" y="81" width="34" height="30" rx="3"/>
      <circle cx="37" cy="133" r="6" fill="var(--blush)"/><text class="label" x="37" y="136" font-size="7" text-anchor="middle">02</text>
      <text class="label" x="48" y="136" font-size="7">LOREM IPSUM IS SIMPLY DUMMY TEXT ?</text>
      <rect class="frame" x="31" y="148" width="34" height="31" rx="3"/>
      <line class="rule" x1="70" y1="154" x2="164" y2="154"/><line class="rule" x1="70" y1="166" x2="164" y2="166"/><line class="rule" x1="70" y1="178" x2="164" y2="178"/>
      <circle cx="37" cy="199" r="6" fill="var(--blush)"/><text class="label" x="37" y="202" font-size="7" text-anchor="middle">03</text>
      <text class="label" x="48" y="202" font-size="7">LOREM IPSUM IS SIMPLY DUMMY TEXT ?</text>
      <line class="rule" x1="31" y1="219" x2="123" y2="219"/><line class="rule" x1="31" y1="231" x2="123" y2="231"/><line class="rule" x1="31" y1="243" x2="123" y2="243"/>
      <rect class="frame" x="130" y="214" width="34" height="30" rx="3"/>
      <circle cx="98" cy="257" r="8" fill="var(--teal)" stroke="var(--paper)" stroke-width="1.2"/>
      <text class="badge-text" x="98" y="260" text-anchor="middle">04</text>
    </svg>
  </article>

  <!-- Page 06: student response -->
  <article class="page" style="left:958px;top:357px;">
    <div class="page-pattern" role="img" aria-label="Light school doodle pattern"></div>
    <div class="page-card"></div>
    <svg viewBox="0 0 196 276">
      <circle cx="162" cy="17" r="9" fill="var(--teal)" stroke="var(--paper)" stroke-width="1.2"/>
      <text class="badge-text" x="162" y="20" text-anchor="middle">06</text>
      <line class="rule" x1="31" y1="41" x2="42" y2="41"/><line class="rule" x1="154" y1="41" x2="165" y2="41"/>
      <text class="heading" x="98" y="47" text-anchor="middle">STUDENTS RESPONSE</text>
      <rect class="frame" x="31" y="60" width="133" height="74" rx="7"/>
      <g>
        <circle cx="40" cy="161" r="9" fill="var(--blush)"/>
        <path d="M40,156 L41.5,159.2 L45,159.5 L42.3,161.8 L43.1,165.2 L40,163.4 L36.9,165.2 L37.7,161.8 L35,159.5 L38.5,159.2 Z" fill="var(--star)"/>
        <line class="rule" x1="59" y1="165" x2="164" y2="165"/>
        <circle cx="40" cy="192" r="9" fill="var(--blush)"/>
        <path d="M40,187 L41.5,190.2 L45,190.5 L42.3,192.8 L43.1,196.2 L40,194.4 L36.9,196.2 L37.7,192.8 L35,190.5 L38.5,190.2 Z" fill="var(--star)"/>
        <line class="rule" x1="59" y1="196" x2="164" y2="196"/>
        <circle cx="40" cy="223" r="9" fill="var(--blush)"/>
        <path d="M40,218 L41.5,221.2 L45,221.5 L42.3,223.8 L43.1,227.2 L40,225.4 L36.9,227.2 L37.7,223.8 L35,221.5 L38.5,221.2 Z" fill="var(--star)"/>
        <line class="rule" x1="59" y1="227" x2="164" y2="227"/>
      </g>
      <circle cx="98" cy="255" r="8" fill="var(--teal)" stroke="var(--paper)" stroke-width="1.2"/>
      <text class="badge-text" x="98" y="258" text-anchor="middle">06</text>
    </svg>
  </article>

</div>
</body>
</html>
```